Need a Brochure Design

We need a brochure designed (A4 two sides or A3 foldable which is equal to 2 x A4 = total of four pages )

Brief and Logo attached.

```html
<!DOCTYPE html>
<html lang="en">
<head>
<meta charset="utf-8">
<title>Staged Well – Brochure</title>
<link href="https://fonts.googleapis.com/css2?family=Montserrat:wght@400;500;600;700&display=swap" rel="stylesheet">
<style>
  :root {
    --tan: #d8bcae;
    --tan-text: #cf9f86;
    --dark: #2b2423;
    --ink: #2e2a29;
    --grey-text: #6d6866;
    --paper: #f7f6f5;
    --backdrop: #d4d4d4;
    --photo-warm: linear-gradient(135deg, #e9e7e4 0%, #c9c3bd 45%, #8a6a4e 100%);
    --photo-room: linear-gradient(160deg, #f1f1ef 0%, #d8d5d0 55%, #a4774d 100%);
    --photo-blue: linear-gradient(150deg, #eef0f1 0%, #7fa9b6 50%, #3f5f6a 100%);
  }
  * { box-sizing: border-box; margin: 0; padding: 0; }
  html, body { width: 1200px; height: 1200px; overflow: hidden; }
  body { background: var(--backdrop); font-family: 'Montserrat', sans-serif; color: var(--ink); position: relative; }

  .spread { position: absolute; left: 210px; width: 780px; height: 551px; display: flex; box-shadow: 0 6px 18px rgba(0,0,0,.18); }
  .spread--outer { top: 34px; }
  .spread--inner { top: 615px; }
  .page { position: relative; width: 390px; height: 551px; background: var(--paper); overflow: hidden; }
  .page + .page { border-left: 1px solid #e2dfdc; }
  .block { position: absolute; }
  .tan { background: var(--tan); }
  .dark { background: var(--dark); color: #fff; }
  .photo { position: absolute; border: 5px solid var(--dark); background: var(--photo-room); }
  .photo--warm { background: var(--photo-warm); }
  .photo--blue { background: var(--photo-blue); }

  /* page 1: about */
  .about { position: absolute; left: 40px; top: 42px; width: 325px; font-size: 8.3px; line-height: 1.4; }
  .about p { margin-bottom: 6px; }
  .about h3 { color: var(--tan-text); font-size: 8.3px; font-weight: 500; text-transform: uppercase; letter-spacing: .3px; margin: 4px 0 3px; }
  .checklist { list-style: none; }
  .checklist li { padding-left: 14px; position: relative; }
  .checklist li::before { content: ""; position: absolute; left: 0; top: 3px; width: 5px; height: 5px; border: 1px solid var(--ink); border-radius: 50%; }
  .referral { left: 20px; right: 0; top: 446px; height: 78px; padding: 10px 18px; font-size: 7.6px; line-height: 1.45; }
  .referral h2 { font-size: 12px; font-weight: 700; margin-bottom: 4px; }
  .referral .site { letter-spacing: 1.2px; font-size: 7px; text-align: center; margin-top: 2px; }

  /* page 2: team */
  .brand { position: absolute; left: 70px; top: 16px; display: flex; align-items: center; gap: 8px; font-size: 13px; font-weight: 500; color: var(--ink); }
  .brand__dot { width: 34px; height: 34px; border-radius: 50%; background: #f1d6c4; }
  .greeting { left: 14px; top: 300px; width: 120px; height: 178px; }
  .greeting h2 { position: absolute; left: 14px; top: 106px; font-size: 12px; font-weight: 500; color: var(--dark); }
  .intro { position: absolute; left: 146px; top: 410px; width: 225px; font-size: 7.5px; line-height: 1.4; }
  .site-bar { left: 14px; right: 10px; top: 448px; height: 30px; display: flex; align-items: center; justify-content: flex-end; padding-right: 20px; font-size: 11px; font-weight: 600; letter-spacing: 1.6px; }

  /* page 3: packages */
  .lead { position: absolute; left: 30px; top: 38px; width: 200px; font-size: 8px; line-height: 1.4; color: var(--grey-text); }
  .lead h2 { color: var(--tan-text); font-size: 9.5px; font-weight: 500; letter-spacing: .4px; margin-bottom: 4px; }
  .package { position: absolute; font-size: 8.3px; line-height: 1.35; color: var(--ink); }
  .package .price { color: var(--tan-text); margin-top: 3px; }
  .package s { color: var(--ink); margin-left: 2px; }

  /* page 4: services */
  .services { position: absolute; left: 40px; top: 272px; width: 330px; font-size: 8px; line-height: 2; }
  .contact { left: 40px; top: 432px; width: 290px; height: 76px; padding: 10px 16px; font-size: 8px; line-height: 1.6; }
  .contact h2 { font-size: 11px; font-weight: 500; margin-bottom: 4px; }
  .contact__row { display: flex; align-items: center; gap: 8px; }
  .contact__row svg { width: 11px; height: 11px; }
</style>
</head>
<body>

<section class="spread spread--outer">
  <article class="page page--about">
    <div class="block tan" style="left:0;top:36px;width:20px;height:515px"></div>
    <div class="block tan" style="left:0;top:524px;width:390px;height:27px"></div>
    <div class="about">
      <p>We are a friendly bunch who are passionate about home staging. We've been property staging apartments, townhouses, and standalone homes since 2009. An all-female powerhouse, we combine our experience in art, interior design, retail, and business to offer professional home styling throughout Melbourne.</p>
      <h3>Because first impressions count</h3>
      <p>A gorgeous looking home sells faster and fetches a higher price.</p>
      <p>At Staged Well, we help our property clients create a lasting impression with minimal spend. Our property vendors are usually looking for home-staging on a tight budget. They come to us searching for creative transformations to help them sell well. Thoughtfully positioned furniture and on-trend interior décor can make all the difference!</p>
      <p>Our property styling service includes a free consultation, longer rental periods and installation and removal.</p>
      <h3>We're well-connected</h3>
      <p>We have a steady flow of clients who have not yet secured their Real Estate Agents, so we'd be happy to share the love. We believe in lasting relationships, and we work with reputable agents across Melbourne.</p>
      <h3>Why choose Staged Well?</h3>
      <ul class="checklist">
        <li>Experienced, enthusiastic property stylists</li>
        <li>Work with low client budgets</li>
        <li>Fast turnaround to a tight deadline</li>
        <li>Flexible rental terms (4/6/8 weeks)</li>
        <li>Happy to recommend potential customers</li>
      </ul>
    </div>
    <div class="block dark referral">
      <h2>We Reward Referrals!</h2>
      <p>We Offer A $200 Gift Voucher For Every Successful Referral To Us!</p>
      <p>We'd Love To Hear From You, So Please Contact Us By:</p>
      <p>Telephone &amp; Text: 0400 555 218</p>
      <p>Email: info@stagedwell.com.au</p>
      <p class="site">Please also visit our website www.stagedwell.com.au</p>
    </div>
  </article>

  <article class="page page--team">
    <div class="block tan" style="left:222px;top:0;width:128px;height:62px"></div>
    <div class="brand"><span class="brand__dot"></span>Staged Well</div>
    <div class="photo photo--warm" style="left:30px;top:62px;width:340px;height:240px" role="img" aria-label="Group photo of the five-woman styling team in white blouses around a mustard armchair"></div>
    <div class="block tan greeting"><h2>HEY THERE</h2></div>
    <p class="intro">I'm Mara, Owner and Creative Director of Staged Well. Please let me introduce you to our amazingly creative property styling team!</p>
    <div class="block dark site-bar">www.stagedwell.com</div>
  </article>
</section>

<section class="spread spread--inner">
  <article class="page page--packages">
    <div class="block tan" style="left:250px;top:0;width:140px;height:100px"></div>
    <div class="block tan" style="left:0;top:400px;width:200px;height:151px"></div>
    <div class="lead">
      <h2>STAGED WELL</h2>
      <p>We average over 185 property styling projects per year, with a large proportion selling in less than 30 days!</p>
    </div>
    <div class="package" style="left:40px;top:104px">
      <p>1 Bedroom Property</p><p>Full Styling + 6 Weeks Free Hire</p>
      <p class="price">$1,897.00 AUD <s>$2,750.00 AUD</s></p>
    </div>
    <div class="photo" style="left:236px;top:62px;width:146px;height:74px" role="img" aria-label="Styled open-plan living and dining room"></div>

    <div class="photo" style="left:70px;top:162px;width:146px;height:74px" role="img" aria-label="Styled bedroom with white bed and window"></div>
    <div class="package" style="left:232px;top:170px">
      <p>2 Bedroom Property</p><p>Full Styling + 6 Weeks Free Hire</p>
      <p class="price">$2,697.00 AUD <s>$3,250.00 AUD</s></p>
    </div>

    <div class="package" style="left:96px;top:276px">
      <p>3 Bedroom Property</p><p>Full Styling + 6 Weeks Free Hire</p>
      <p class="price">$2,997.00 AUD <s>$4,470.00 AUD</s></p>
    </div>
    <div class="photo photo--blue" style="left:250px;top:252px;width:136px;height:76px" role="img" aria-label="Styled lounge with blue accents"></div>

    <div class="photo" style="left:50px;top:380px;width:150px;height:80px" role="img" aria-label="Styled living room with grey sofa"></div>
    <div class="package" style="left:222px;top:396px">
      <p>4 Bedroom Property</p><p>Full Styling + 6 Weeks Free Hire</p>
      <p class="price">$3,897.00 AUD <s>$5,495.00 AUD</s></p>
    </div>
  </article>

  <article class="page page--services">
    <div class="block tan" style="left:0;top:0;width:60px;height:150px"></div>
    <div class="block" style="left:60px;top:0;width:330px;height:168px;background:var(--photo-room)" role="img" aria-label="Two stylists dressing a bed in a bright bedroom"></div>
    <div class="photo" style="left:10px;top:190px;width:112px;height:66px" role="img" aria-label="Styled kitchen and dining area"></div>
    <div class="photo photo--blue" style="left:128px;top:178px;width:74px;height:56px" role="img" aria-label="Styled lounge corner"></div>
    <div class="photo photo--warm" style="left:208px;top:170px;width:140px;height:60px" role="img" aria-label="Outdoor patio with table and chairs"></div>
    <div class="services">
      <p>Helping your property reach its highest potential without busting the budget.</p>
      <p>Achieving a record number of viewings and the highest possible sale price.</p>
      <p>Installation, interior design and decoration, and removal included.</p>
      <p>Pre-sale home preparation to post-sale removal.</p>
      <p>Free consultation and longer rental periods.</p>
      <p>A small investment for such a large transformation!</p>
    </div>
    <div class="block tan" style="left:290px;top:318px;width:100px;height:130px"></div>
    <div class="block dark contact">
      <h2>Please contact us on:</h2>
      <div class="contact__row">
        <svg viewBox="0 0 24 24" fill="none" stroke="#fff" stroke-width="2"><path d="M5 3h4l2 5-3 2a12 12 0 0 0 6 6l2-3 5 2v4a2 2 0 0 1-2 2A18 18 0 0 1 3 5a2 2 0 0 1 2-2z"/></svg>
        <span>0400 555 218</span>
      </div>
      <div class="contact__row">
        <svg viewBox="0 0 24 24" fill="none" stroke="#fff" stroke-width="2"><rect x="3" y="5" width="18" height="14"/><path d="M3 5l9 8 9-8"/></svg>
        <span>info@stagedwell.com.au</span>
      </div>
    </div>
  </article>
</section>

</body>
</html>
```